43 Year Old Construction firm needs Updated Business Card & Stationery Design

We are an established and well known (in our market) commercial construction firm. We need a cleaner and more modern look for our corporate identity material. We would like to continue to use our current colors and logo.
We are thinking about incorporating a slogan on our business card (either front or back): "Striving to be the most trusted builder in our market." The text could change at some point. Our website is www.kradworth.example . Sample card is attached. Some will have more phone numbers, etc...
Updates

Target Market(s)

Commercial and institutional clients.

Industry/Entity Type

Construction Company

Contact Information for Business Card

See attached for existing card. But don't be constrained.

Requirements
Must have
• Logo, name, title, address, website, email, phone numbers (as few as one, as many as three)
• Slogan on front or back "Striving to be the most trusted builder in our market"
• Use existing logo and colors

```html
<!DOCTYPE html>
<html lang="en">
<head>
<meta charset="utf-8">
<title>Kradworth Builders – Stationery</title>
<link href="https://fonts.googleapis.com/css2?family=Open+Sans:wght@400;600;700&display=swap" rel="stylesheet">
<style>
  :root {
    --brand-blue: #144a86;
    --brand-green: #1f9a4d;
    --paper: #ffffff;
    --backdrop: #d9d9d9;
    --ink-light: #ffffff;
  }
  * { box-sizing: border-box; margin: 0; padding: 0; }
  html, body { width: 1200px; height: 1037px; overflow: hidden; }
  body {
    background: var(--backdrop);
    font-family: "Open Sans", Arial, sans-serif;
    position: relative;
  }

  /* Letterhead */
  .letterhead {
    position: absolute; left: 90px; top: 156px;
    width: 560px; height: 725px;
    background: var(--paper);
    box-shadow: 0 6px 22px rgba(0,0,0,.18);
    overflow: hidden;
  }
  .letterhead__header, .letterhead__footer { position: absolute; left: 0; width: 560px; }
  .letterhead__header { top: 0; height: 86px; }
  .letterhead__footer { bottom: 0; height: 112px; }
  .brand-name {
    position: absolute; color: var(--ink-light);
    font-weight: 700; line-height: 1; letter-spacing: .5px;
  }
  .letterhead .brand-name { left: 26px; top: 24px; font-size: 26px; }
  .letterhead__web {
    position: absolute; right: 18px; top: 10px;
    color: var(--ink-light); font-size: 9px; letter-spacing: 2px;
  }
  .letterhead__contact {
    position: absolute; left: 22px; bottom: 14px;
    color: var(--ink-light); font-size: 10px; line-height: 1.55;
  }
  .contact-line { display: flex; align-items: center; gap: 6px; }
  .contact-icon { width: 9px; height: 9px; background: var(--brand-green); border-radius: 1px; flex: none; }

  /* Business cards */
  .card {
    position: absolute; left: 700px;
    width: 420px; height: 240px;
    box-shadow: 0 6px 18px rgba(0,0,0,.2);
    overflow: hidden;
  }
  .card--back { top: 220px; background: var(--brand-blue); }
  .card--front { top: 520px; background: var(--paper); }
  .card svg { position: absolute; left: 0; top: 0; }
  .card--back .brand-name { left: 0; right: 0; top: 98px; text-align: center; font-size: 36px; }

  .card__logo-box {
    position: absolute; right: 22px; top: 24px;
    width: 170px; height: 74px; background: var(--brand-blue);
    border-bottom: 6px solid var(--brand-green);
  }
  .card__logo-box .brand-name { left: 0; right: 0; top: 24px; text-align: center; font-size: 20px; }
  .card__band {
    position: absolute; left: 0; bottom: 0; width: 100%; height: 108px;
    background: var(--brand-blue); color: var(--ink-light);
    padding: 16px 22px; display: flex; justify-content: space-between;
  }
  .card__person-name { color: var(--brand-green); font-size: 14px; font-weight: 600; letter-spacing: .5px; }
  .card__title { font-size: 8px; margin-bottom: 12px; }
  .card__details { font-size: 8.5px; line-height: 1.7; }
  .card__address { font-size: 8.5px; line-height: 1.6; text-align: right; padding-top: 4px; }
</style>
</head>
<body>

<section class="letterhead" aria-label="Letterhead">
  <svg class="letterhead__header" viewBox="0 0 560 86" width="560" height="86" aria-hidden="true">
    <polygon points="0,0 560,0 560,86 0,86" fill="var(--brand-blue)"/>
    <polygon points="0,78 560,30 560,86 0,86" fill="var(--brand-blue)"/>
    <line x1="0" y1="76" x2="560" y2="30" stroke="var(--brand-green)" stroke-width="5"/>
  </svg>
  <div class="brand-name">Kradworth Builders</div>
  <div class="letterhead__web">www.kradworth.example</div>

  <svg class="letterhead__footer" viewBox="0 0 560 112" width="560" height="112" aria-hidden="true">
    <polygon points="232,14 240,0 560,0 560,12" fill="var(--brand-green)"/>
    <polygon points="0,30 228,30 236,17 560,17 560,112 0,112" fill="var(--brand-blue)"/>
  </svg>
  <div class="letterhead__contact">
    <div class="contact-line"><span class="contact-icon"></span>555-014-2290</div>
    <div class="contact-line"><span class="contact-icon"></span>daniel@kradworth.example</div>
    <div>1820 FIELDSTONE AVENUE, BROOKHAVEN, MO 63011-4400</div>
  </div>
</section>

<section class="card card--back" aria-label="Business card back">
  <svg viewBox="0 0 420 240" width="420" height="240" aria-hidden="true">
    <line x1="0" y1="200" x2="420" y2="40" stroke="var(--brand-green)" stroke-width="5"/>
  </svg>
  <div class="brand-name">Kradworth Builders</div>
</section>

<section class="card card--front" aria-label="Business card front">
  <div class="card__logo-box"><div class="brand-name">Kradworth Builders</div></div>
  <div class="card__band">
    <div>
      <div class="card__person-name">DANIEL R. HOLLISTER</div>
      <div class="card__title">President</div>
      <div class="card__details">
        <div class="contact-line"><span class="contact-icon"></span>555-014-2290</div>
        <div class="contact-line"><span class="contact-icon"></span>daniel@kradworth.example</div>
      </div>
    </div>
    <div class="card__address">1820 FIELDSTONE AVENUE<br>BROOKHAVEN, MO 63011-4400</div>
  </div>
</section>

</body>
</html>
```